Construction Company Website Design

I need a Website Design for a Construction Company. I have attached logo and business card design files (a.i) to match styles and text for the website. I will need design for 3 pages:
1. A Home page
2. A secondary page (will be different information pages)
3. A contact page with submision form
Website to look professional and match the 'theme' across all pages, using main colours / reverse colours as per design files. Must be clear it is a construction related website without being over the top. Happy for the construction related details (whether that be images/outlines/backgrounds etc to be fairly subtle and not overbearing on the contect of the pages. It will be the content that will be most important, not the images within.

Content has not yet been fully completed but attached is a site map. Each page will need a space for the insertion of the relevant heading and associated content for that particular page. Example can be used as per attached map. If it is preferable to have content completed for this to be a more succesful project please advise and I will complete and submit.

Target Market(s)

Clients for potential construction projects. These could be a range of people. All would be very professional, well educated and put a substantial expection on the quality of website provided.

Industry/Entity Type

Construction

Number of Pages Required

3 page

Font styles to use
Serif
Sans Serif
Other font styles liked:
• fonts preferable as per design files provided unless designer beleives a different font would suit better

Requirements
Must have
• Colour scheme to match logo and business card files provided. Fonts that match as per provided files. Pages must be consistent with the theme carrying across all pages. All pages must have contact details at the bottom of the page.
• Contents of page 1 - 'Home page': multiple tab options / logo link
• Contents of page 2 - 'Secondary page': Top and side navigation / area for information and/or images.
• Contents of page - 'Contact us page': Top and side navigation / Submission form / area for logos such as linkdin, facebook etc.
Nice to have
• Would be good to have a or some generic construction related images - outlines / shadows / effects etc. These might be background images or outlines related to the relevant industry and are consistent across the pages. Could be outlines of buildings, images of men with hardhats etc etc. Good to see colour scheme as per design files used
Should not have
• No pictures of houses. Generally no photos. If any imagery of people must not show faces/details.

```html
<!DOCTYPE html>
<html lang="en">
<head>
<meta charset="utf-8">
<title>Halvard Constructions</title>
<link href="https://fonts.googleapis.com/css2?family=Roboto:wght@300;400;500;700&family=Open+Sans:wght@400;600;700&display=swap" rel="stylesheet">
<style>
:root{
  --blue:#1a87d8;
  --blue-dark:#0f6fbf;
  --navy:#0b2f66;
  --ink:#222;
  --muted:#666;
  --line:#d8d8d8;
  --pale:#e9f1f7;
  --dark:#232323;
  --white:#fff;
  --star:#f2d21b;
}
*{box-sizing:border-box;margin:0;padding:0}
html,body{width:1200px;height:3543px;overflow:hidden}
body{font-family:"Open Sans",Arial,sans-serif;color:var(--ink);background:var(--white);position:relative}
.section{position:absolute;left:0;width:1200px}
h2.section-title{font-family:"Roboto",Arial,sans-serif;font-weight:300;font-size:33px;text-align:center;color:var(--ink)}
h2.section-title b{font-weight:700}

/* header */
.site-header{top:0;height:95px;background:var(--white)}
.brand{position:absolute;left:97px;top:30px;font-family:"Roboto",Arial,sans-serif;font-weight:400;font-size:24px;letter-spacing:2px;color:#333;display:flex;align-items:center;gap:12px}
.brand-mark{width:14px;height:14px;background:var(--blue)}
.top-contact{position:absolute;right:97px;top:16px;font-size:16px;font-weight:600;color:#333;display:flex;gap:14px;align-items:center}
.top-contact svg{vertical-align:-3px;margin-right:6px}
.main-nav{position:absolute;right:97px;top:64px;display:flex;gap:27px;font-family:"Roboto",Arial,sans-serif;font-weight:500;font-size:15px;color:#333;align-items:center}
.main-nav .active{color:var(--blue)}

/* hero */
.hero{top:95px;height:505px;background:linear-gradient(120deg,#0a2a5e 0%,#1a5fb0 55%,#0d3773 100%)}
.hero-art{position:absolute;inset:0}
.hero h1{position:absolute;top:125px;width:100%;text-align:center;font-family:"Roboto",Arial,sans-serif;color:var(--white);font-size:68px;font-weight:300;letter-spacing:1px}
.hero h1 b{font-weight:700}
.hero p{position:absolute;top:218px;width:100%;text-align:center;color:var(--white);font-size:22px;font-weight:600;line-height:33px}
.btn-outline-light{position:absolute;top:310px;left:505px;width:190px;height:48px;border:2px solid var(--white);border-radius:24px;color:var(--white);font-family:"Roboto",Arial,sans-serif;font-weight:700;font-size:16px;display:flex;align-items:center;justify-content:center}
.slider-dots{position:absolute;top:443px;left:0;width:100%;display:flex;justify-content:center;gap:6px}
.slider-dots span{width:12px;height:12px;border-radius:50%;border:2px solid var(--white)}
.slider-dots span.on{background:var(--white)}

/* welcome */
.welcome{top:600px;height:568px}
.welcome-media{position:absolute;left:97px;top:116px;width:483px;height:324px;background:linear-gradient(135deg,#1c2c46,#6d8098 60%,#2b3d58)}
.play{position:absolute;left:213px;top:134px}
.welcome-card{position:absolute;left:498px;top:76px;width:602px;height:404px;border:1px solid #bfbfbf;padding:38px 32px 0 122px}
.welcome-card h3{font-family:"Roboto",Arial,sans-serif;font-weight:400;font-size:31px;color:var(--ink)}
.welcome-card h3 b{font-weight:700}
.welcome-card p{margin-top:22px;font-size:13.5px;line-height:25px;color:#555}
.btn-outline{display:inline-flex;align-items:center;justify-content:center;border:2px solid var(--blue);color:var(--blue);border-radius:24px;font-family:"Roboto",Arial,sans-serif;font-weight:700;font-size:15px;height:46px}
.welcome-card .btn-outline{margin-top:28px;width:136px}

/* services */
.services{top:1168px;height:532px;background:linear-gradient(180deg,#e4eef5,#f2f7fa)}
.services .section-title{position:absolute;top:64px;width:100%}
.service{position:absolute;top:137px;width:240px;text-align:center}
.service-ring{width:194px;height:194px;margin:0 auto;border-radius:50%;border:4px solid var(--blue);display:flex;align-items:center;justify-content:center}
.service-ring div{width:170px;height:170px;border-radius:50%;border:3px solid var(--blue);background:var(--white);display:flex;align-items:center;justify-content:center}
.service h4{margin-top:18px;font-family:"Roboto",Arial,sans-serif;font-weight:500;font-size:23px;color:var(--ink)}
.service p{margin-top:12px;font-size:14px;line-height:24px;color:#666}

/* testimonials */
.testimonials{top:1700px;height:410px;background:linear-gradient(180deg,#1f8ee0,#1573c4)}
.testimonials .section-title{position:absolute;top:75px;width:100%;color:var(--white)}
.quote{position:absolute;top:160px;width:330px;height:170px}
.avatar{position:absolute;left:0;top:0;width:78px;height:78px;border-radius:50%;background:#dfe6ec;border:3px solid var(--white)}
.quote-body{position:absolute;left:93px;top:0;color:var(--white)}
.quote-body p{font-size:11.5px;font-style:italic;line-height:24px}
.quote-body p::before{content:"\201C";font-family:Georgia,serif;font-size:30px;font-weight:700;font-style:normal;vertical-align:-10px;margin-right:6px}
.quote-name{margin-top:12px;font-size:11px;font-weight:700;text-transform:uppercase}
.quote-role{font-size:10px;font-style:italic}
.stars{position:absolute;left:90px;top:150px;display:flex;gap:6px}
.nav-arrow{position:absolute;top:215px;width:36px;height:36px;border-radius:50%;border:2px solid var(--white);display:flex;align-items:center;justify-content:center}

/* projects */
.projects{top:2110px;height:855px}
.projects .section-title{position:absolute;top:80px;width:100%}
.project-grid{position:absolute;top:160px;left:0;width:1200px;display:grid;grid-template-columns:repeat(4,294px);grid-template-rows:250px 250px;gap:8px 8px}
.project-tile{width:100%;height:100%}
.projects .btn-outline{position:absolute;top:714px;left:520px;width:160px;height:54px}

/* contact */
.contact{top:2965px;height:578px;background:linear-gradient(160deg,#2b2b2b,#1c1c1c)}
.contact .section-title{position:absolute;top:64px;width:100%;color:var(--white)}
.label-head{font-size:15px;font-weight:700;color:var(--white);text-transform:uppercase}
.contact-form{position:absolute;left:97px;top:135px;width:633px}
.field-label{display:block;font-size:11px;color:var(--white);text-transform:uppercase;margin:36px 0 8px}
.field{height:33px;background:var(--white)}
.row{display:flex;gap:9px}
.row>div{flex:1}
.row .field-label{margin-top:36px}
.field.msg{height:82px}
.btn-submit{position:absolute;right:0;top:356px;width:100px;height:34px;background:var(--blue);color:var(--white);border-radius:17px;font-size:13px;font-weight:700;display:flex;align-items:center;justify-content:center}
.contact-info{position:absolute;left:808px;top:135px;width:300px}
.info-item{display:flex;align-items:flex-start;gap:22px;color:var(--white);font-size:13.5px;line-height:24px;margin-top:22px}
.info-item:first-of-type{margin-top:26px}
.info-icon{flex:none;width:38px;height:38px;border-radius:50%;border:2px solid var(--white);display:flex;align-items:center;justify-content:center}
.social-head{margin-top:34px}
.social{display:flex;gap:14px;margin-top:20px}
.social span{width:26px;height:26px;background:var(--white);border-radius:4px}
.footer-rule{position:absolute;left:97px;top:500px;width:1006px;height:1px;background:#444}
.copyright{position:absolute;top:530px;width:100%;text-align:center;color:var(--white);font-size:14px}
</style>
</head>
<body>

<header class="section site-header">
  <div class="brand"><span class="brand-mark"></span>HALVARD CONSTRUCTIONS</div>
  <div class="top-contact">
    <span><svg width="16" height="16" viewBox="0 0 24 24"><path fill="#1a87d8" d="M6.6 10.8a15 15 0 0 0 6.6 6.6l2.2-2.2a1 1 0 0 1 1-.25 11.4 11.4 0 0 0 3.6.57 1 1 0 0 1 1 1V20a1 1 0 0 1-1 1A17 17 0 0 1 3 4a1 1 0 0 1 1-1h3.5a1 1 0 0 1 1 1c0 1.25.2 2.45.57 3.57a1 1 0 0 1-.25 1z"/></svg>1 800 555 0148</span>
    <span>|</span>
    <span><svg width="18" height="16" viewBox="0 0 24 20"><rect x="1" y="2" width="22" height="16" rx="2" fill="#1a87d8"/><path d="M2 4l10 7 10-7" stroke="#fff" stroke-width="2" fill="none"/></svg>info@halvardbuild.example</span>
  </div>
  <nav class="main-nav">
    <span class="active">HOME</span><span>ABOUT US</span><span>SERVICES</span><span>PROJECTS</span><span>CULTURE</span><span>NEWS</span><span>CONTACT</span>
    <svg width="16" height="16" viewBox="0 0 24 24"><circle cx="10" cy="10" r="7" stroke="#333" stroke-width="3" fill="none"/><path d="M15 15l7 7" stroke="#333" stroke-width="3"/></svg>
  </nav>
</header>

<section class="section hero">
  <div class="hero-art" role="img" aria-label="Blueprint-style background of building outlines in deep blue"></div>
  <h1><b>HALVARD</b> CONSTRUCTIONS</h1>
  <p>At vero eos et accusamus et iusto odio dignissimos ducimus<br>qui blanditiis praesentium voluptatum dele</p>
  <div class="btn-outline-light">GET MORE INFO</div>
  <div class="slider-dots"><span class="on"></span><span></span><span></span><span></span></div>
</section>

<section class="section welcome">
  <div class="welcome-media" role="img" aria-label="Video still of a wireframe building model">
    <svg class="play" width="56" height="56" viewBox="0 0 56 56"><circle cx="28" cy="28" r="26" fill="#111" stroke="#fff" stroke-width="3"/><path d="M22 16l18 12-18 12z" fill="#fff"/></svg>
  </div>
  <div class="welcome-card">
    <h3><b>Welcome to</b> Halvard Constructions</h3>
    <p>Nam libero tempore, cum soluta nobis est eligendi optio cumque nihil impedit quo minus id quod maxime placeat facere possimus, omnis vol uptas assumenda est, omnis dolor repellendus. Temporibus autem qui busdam et aut officiis debitis aut rerum necessitatibus saepe eveniet ut et voluptates repudiandae sint et molestiae non recusandae. Itaque ear um rerum hic tenetur a sapiente delectus, ut aut reiciendis voluptatibus maiores alias consequatur aut.</p>
    <div class="btn-outline">READ MORE</div>
  </div>
</section>

<section class="section services">
  <h2 class="section-title"><b>Our</b> Services</h2>
  <div class="service" style="left:94px">
    <div class="service-ring"><div><svg width="60" height="70" viewBox="0 0 60 70"><rect x="10" y="4" width="40" height="62" fill="#1a87d8"/><g fill="#fff"><rect x="17" y="12" width="7" height="7"/><rect x="27" y="12" width="7" height="7"/><rect x="37" y="12" width="7" height="7"/><rect x="17" y="24" width="7" height="7"/><rect x="27" y="24" width="7" height="7"/><rect x="37" y="24" width="7" height="7"/><rect x="17" y="36" width="7" height="7"/><rect x="27" y="36" width="7" height="7"/><rect x="37" y="36" width="7" height="7"/><rect x="25" y="50" width="10" height="16"/></g></svg></div></div>
    <h4>Commercial</h4>
    <p>Nam libero tempptaore, cum so luta nobis est eligendi optio cumque nihil imppendit quo minu.</p>
  </div>
  <div class="service" style="left:352px">
    <div class="service-ring"><div><svg width="66" height="66" viewBox="0 0 66 66"><path d="M44 6a16 16 0 0 0-15 21L8 48a6 6 0 0 0 9 9l21-21a16 16 0 0 0 21-15l-9 9-9-3-3-9 9-9a16 16 0 0 0-3-3z" fill="#1a87d8"/></svg></div></div>
    <h4>Building Maintenance</h4>
    <p>Nam libero tempptaore, cum so luta nobis est eligendi optio cumque nihil imppendit quo minu.</p>
  </div>
  <div class="service" style="left:608px">
    <div class="service-ring"><div><svg width="72" height="64" viewBox="0 0 72 64"><path d="M36 4L2 34h10v28h18V44h12v18h18V34h10z" fill="#1a87d8"/></svg></div></div>
    <h4>Residential</h4>
    <p>Nam libero tempptaore, cum so luta nobis est eligendi optio cumque nihil imppendit quo minu.</p>
  </div>
  <div class="service" style="left:866px">
    <div class="service-ring"><div><svg width="76" height="70" viewBox="0 0 76 70"><g fill="#1a87d8"><circle cx="28" cy="40" r="17"/><g stroke="#1a87d8" stroke-width="8"><path d="M28 16v48M4 40h48M11 23l34 34M45 23L11 57"/></g><circle cx="58" cy="20" r="10"/><g stroke="#1a87d8" stroke-width="5"><path d="M58 5v30M43 20h30M47 9l22 22M69 9L47 31"/></g></g><circle cx="28" cy="40" r="7" fill="#fff"/><circle cx="58" cy="20" r="4" fill="#fff"/></svg></div></div>
    <h4>Project Management</h4>
    <p>Nam libero tempptaore, cum so luta nobis est eligendi optio cumque nihil imppendit quo minu.</p>
  </div>
</section>

<section class="section testimonials">
  <h2 class="section-title"><b>Client</b> Testimonials</h2>
  <div class="nav-arrow" style="left:28px"><svg width="12" height="14" viewBox="0 0 12 14"><path d="M9 1L3 7l6 6" stroke="#fff" stroke-width="2" fill="none"/></svg></div>
  <div class="nav-arrow" style="right:28px"><svg width="12" height="14" viewBox="0 0 12 14"><path d="M3 1l6 6-6 6" stroke="#fff" stroke-width="2" fill="none"/></svg></div>

  <div class="quote" style="left:97px">
    <div class="avatar" role="img" aria-label="Client portrait placeholder"></div>
    <div class="quote-body">
      <p>At vero eos et accusamus et iustodio<br>dignissimos ducimus qui blanditiipraesent<br>ium voluptatum deleniti atq.</p>
      <div class="quote-name">Mara Ellison</div>
      <div class="quote-role">Financial Services Professional</div>
    </div>
    <div class="stars"><svg width="110" height="18" viewBox="0 0 110 18"><g fill="#f2d21b"><path id="st" d="M9 1l2.4 5 5.6.8-4 3.9 1 5.5L9 13.6 4 16.2l1-5.5-4-3.9L6.6 6z"/><use href="#st" x="23"/><use href="#st" x="46"/><use href="#st" x="69"/></g><use href="#st" x="92" fill="none" stroke="#f2d21b" stroke-width="1.3"/></svg></div>
  </div>

  <div class="quote" style="left:443px">
    <div class="avatar" role="img" aria-label="Client portrait placeholder"></div>
    <div class="quote-body">
      <p>At vero eos et accusamus et iustodio<br>dignissimos ducimus qui blanditiipraesent<br>ium voluptatum deleniti atqu.</p>
      <div class="quote-name">Tobias R. Hale</div>
      <div class="quote-role">National Urban Fellow at the Institute</div>
    </div>
    <div class="stars"><svg width="110" height="18" viewBox="0 0 110 18"><g fill="#f2d21b"><use href="#st"/><use href="#st" x="23"/><use href="#st" x="46"/><use href="#st" x="69"/><path d="M101 1v12.6L96 16.2l1-5.5-4-3.9 5.6-.8z"/></g></svg></div>
  </div>

  <div class="quote" style="left:789px">
    <div class="avatar" role="img" aria-label="Client portrait placeholder"></div>
    <div class="quote-body">
      <p>At vero eos et accusamus et iustodio<br>dignissimos ducimus qui blanditiipraesent<br>ium voluptatum deleniti atqu.</p>
      <div class="quote-name">Petra Lindqvist</div>
      <div class="quote-role">Creative Strategist | Entrepreneur &amp; Upcoming</div>
    </div>
    <div class="stars"><svg width="110" height="18" viewBox="0 0 110 18"><g fill="#f2d21b"><use href="#st"/><use href="#st" x="23"/><use href="#st" x="46"/><use href="#st" x="69"/></g><use href="#st" x="92" fill="none" stroke="#f2d21b" stroke-width="1.3"/></svg></div>
  </div>
</section>

<section class="section projects">
  <h2 class="section-title"><b>Our</b> Projects</h2>
  <div class="project-grid">
    <div class="project-tile" role="img" aria-label="Blue 3D building model render" style="background:linear-gradient(135deg,#0c2c6e,#1e6be0 50%,#0d2f6a)"></div>
    <div class="project-tile" role="img" aria-label="Apartment building render" style="background:linear-gradient(180deg,#d9dee4,#7c858c 60%,#9aa38a)"></div>
    <div class="project-tile" role="img" aria-label="Wireframe building drawing in blue" style="background:linear-gradient(160deg,#0f3f7a,#3f7fc2)"></div>
    <div class="project-tile" role="img" aria-label="Curved commercial building model" style="background:linear-gradient(180deg,#c6ccd0,#b9bfae 60%,#7d8a6c)"></div>
    <div class="project-tile" role="img" aria-label="White city block massing model" style="background:linear-gradient(180deg,#b7c7d6,#e9edf0 55%,#c3c8cc)"></div>
    <div class="project-tile" role="img" aria-label="Floor plan cutaway model" style="background:linear-gradient(180deg,#8f8f8f,#6e5e54 50%,#9a9a9a)"></div>
    <div class="project-tile" role="img" aria-label="Line sketch of a building" style="background:linear-gradient(180deg,#f4f4f4,#c9c9c9)"></div>
    <div class="project-tile" role="img" aria-label="Blueprint of a building" style="background:linear-gradient(135deg,#0a3b8f,#1d5cc2)"></div>
  </div>
  <div class="btn-outline">VIEW MORE</div>
</section>

<section class="section contact">
  <h2 class="section-title"><b>Contact</b> Us</h2>
  <div class="contact-form">
    <div class="label-head">Contact Form</div>
    <div class="row">
      <div><span class="field-label">Name :</span><div class="field"></div></div>
      <div><span class="field-label">Phone No :</span><div class="field"></div></div>
    </div>
    <span class="field-label" style="margin-top:18px">Email :</span><div class="field"></div>
    <span class="field-label" style="margin-top:18px">Message :</span><div class="field msg"></div>
    <div class="btn-submit">SUBMIT</div>
  </div>
  <div class="contact-info">
    <div class="label-head">Contact Information</div>
    <div class="info-item"><span class="info-icon"><svg width="14" height="18" viewBox="0 0 14 18"><path d="M7 0a7 7 0 0 0-7 7c0 5 7 11 7 11s7-6 7-11a7 7 0 0 0-7-7z" fill="#fff"/><circle cx="7" cy="7" r="2.5" fill="#232323"/></svg></span><span>We are located at 12 Ardent Lane in<br>Brookvale, Victoria</span></div>
    <div class="info-item"><span class="info-icon"><svg width="16" height="16" viewBox="0 0 24 24"><path fill="#fff" d="M6.6 10.8a15 15 0 0 0 6.6 6.6l2.2-2.2a1 1 0 0 1 1-.25 11.4 11.4 0 0 0 3.6.57 1 1 0 0 1 1 1V20a1 1 0 0 1-1 1A17 17 0 0 1 3 4a1 1 0 0 1 1-1h3.5a1 1 0 0 1 1 1c0 1.25.2 2.45.57 3.57a1 1 0 0 1-.25 1z"/></svg></span><span style="padding-top:6px">0400 555 271</span></div>
    <div class="info-item"><span class="info-icon"><svg width="18" height="14" viewBox="0 0 24 18"><rect x="1" y="1" width="22" height="16" rx="2" fill="#fff"/><path d="M2 3l10 7 10-7" stroke="#232323" stroke-width="2" fill="none"/></svg></span><span style="padding-top:6px">office@halvardbuild.example</span></div>
    <div class="label-head social-head">Social</div>
    <div class="social"><span></span><span></span><span></span><span></span></div>
  </div>
  <div class="footer-rule"></div>
  <div class="copyright">Copyrights © 2018, Halvard Constructions . All Rights Reserved.</div>
</section>

</body>
</html>
```